Vornel Technologies business card design

We need a business card designed with our new logo. it would be great if the card could communicate it is a technology based company.

Target Market(s)

system integrators

Industry/Entity Type

technology, IOT

Contact Information for Business Card

Name, designation, Address, telephone number, email address

Requirements
Must have
• logo and company name
Nice to have
• something to do with technology

```html
<!DOCTYPE html>
<html lang="en">
<head>
<meta charset="utf-8">
<title>Vornel Technologies – Business Card</title>
<link href="https://fonts.googleapis.com/css2?family=Arimo:wght@400;700&display=swap" rel="stylesheet">
<style>
  :root {
    --page-bg: #1c1c1c;
    --card-bg: #333333;
    --pattern-bg: #2e2e2e;
    --pattern-tone: #3a3a3a;
    --accent: #f7941d;
    --ink: #ffffff;
    --ink-soft: #e6e6e6;
  }
  * { box-sizing: border-box; margin: 0; padding: 0; }
  html, body {
    width: 1200px; height: 900px; overflow: hidden;
    background: var(--page-bg);
    font-family: "Arimo", Arial, sans-serif;
  }
  .sheet {
    width: 1200px; height: 900px;
    display: flex; flex-direction: column; align-items: center; justify-content: center;
    gap: 40px;
  }
  .card {
    position: relative;
    width: 700px; height: 400px;
    border-radius: 26px;
    overflow: hidden;
    background: var(--card-bg);
    box-shadow: 0 14px 30px rgba(0,0,0,.45);
  }
  /* front */
  .card-front { border-bottom: 12px solid var(--accent); }
  .person { position: absolute; left: 56px; top: 118px; }
  .person-name {
    color: var(--accent); font-weight: 700; font-size: 30px; line-height: 1;
    letter-spacing: .5px; text-transform: uppercase;
  }
  .person-role { color: var(--ink-soft); font-size: 17px; line-height: 1; margin-top: 8px; }
  .divider {
    position: absolute; left: 56px; right: 56px; top: 190px;
    height: 1.5px; background: var(--accent);
  }
  .contacts { position: absolute; left: 56px; top: 214px; list-style: none; }
  .contacts li {
    display: flex; align-items: center; gap: 10px;
    color: var(--ink-soft); font-size: 17px; line-height: 1; margin-bottom: 13px;
  }
  .contacts svg { width: 15px; height: 15px; flex: none; }
  .brand-front {
    position: absolute; right: 56px; top: 96px;
    display: flex; align-items: center; gap: 14px;
  }
  .brand-mark { width: 30px; height: 30px; background: var(--accent); flex: none; }
  .brand-name {
    color: var(--ink); font-weight: 700; font-size: 28px;
    line-height: 1.1; text-transform: uppercase; letter-spacing: 1px;
  }
  .address {
    position: absolute; right: 56px; bottom: 28px; text-align: right;
    font-style: normal;
    color: var(--ink-soft); font-size: 17px; line-height: 1.35;
  }
  /* back */
  .card-back { background: var(--pattern-bg); }
  .pattern-field {
    position: absolute; inset: 0;
    background: linear-gradient(135deg, var(--pattern-tone), var(--pattern-bg) 60%, #343434);
  }
  .brand-back {
    position: absolute; left: 56px; bottom: 56px;
    display: flex; align-items: center; gap: 12px;
  }
  .brand-back .brand-mark { width: 24px; height: 24px; }
  .brand-back .brand-name { font-size: 24px; }
</style>
</head>
<body>
<main class="sheet">
  <section class="card card-front" aria-label="Business card front">
    <div class="person">
      <h1 class="person-name">Daniel Marsh</h1>
      <p class="person-role">CEO/Founder</p>
    </div>
    <div class="brand-front">
      <span class="brand-mark"></span>
      <span class="brand-name">Vornel<br>Technologies</span>
    </div>
    <div class="divider"></div>
    <ul class="contacts">
      <li>
        <svg viewBox="0 0 16 16" aria-hidden="true"><path d="M3 1.5l2.6.4 1 3-1.5 1.2a8 8 0 0 0 4.3 4.3l1.2-1.5 3 1 .4 2.6-1.5 1.5C7 13.6 2.4 9 1.5 3z" fill="var(--accent)"/></svg>
        (123) 555-0148
      </li>
      <li>
        <svg viewBox="0 0 16 16" aria-hidden="true"><rect x="1" y="3" width="14" height="10" rx="1" fill="var(--accent)"/><path d="M1.5 3.8L8 8.6l6.5-4.8" stroke="var(--card-bg)" stroke-width="1.3" fill="none"/></svg>
        info@vorneltechnologies.com
      </li>
      <li>
        <svg viewBox="0 0 16 16" aria-hidden="true"><g fill="none" stroke="var(--accent)" stroke-width="1.4"><circle cx="8" cy="8" r="6.5"/><ellipse cx="8" cy="8" rx="2.8" ry="6.5"/><path d="M1.5 8h13"/></g></svg>
        www.vorneltechnologies.com
      </li>
    </ul>
    <address class="address">2190 Street Name<br>Country Name AB 4410</address>
  </section>

  <section class="card card-back" aria-label="Business card back">
    <div class="pattern-field" role="img" aria-label="Tone-on-tone repeating brand pattern"></div>
    <div class="brand-back">
      <span class="brand-mark"></span>
      <span class="brand-name">Vornel<br>Technologies</span>
    </div>
  </section>
</main>
</body>
</html>
```